Splash Screen for a new release of software

Our company Tarnwell Asia Pacific writes business management software for the automotive industry. Early next year we are planning on releasing our new version of Velquira, this is a fourth generation product. Our thoughts are to brand this version simply Velquira 4, however we do wish to add a certain exclusivity to product hence the addition of Premier Edition as a signature to the Velquira brand. The splash screen has to make the user feel that they are using an upmarket product and are excited to be doing so. I have uploaded an "in house" design for reference purposes, also included our sphere company logo.

```html
<!DOCTYPE html>
<html lang="en">
<head>
<meta charset="utf-8">
<title>Velquira 4 – Premier Edition Splash Screen</title>
<link href="https://fonts.googleapis.com/css2?family=Playfair+Display:wght@400&family=Raleway:wght@400;500&family=Montserrat:wght@400;700&display=swap" rel="stylesheet">
<style>
  :root {
    --page: #ffffff;
    --card-left: #6a4a8c;
    --card-right: #3e3d70;
    --glow: #b34dff;
    --ring-dark: #2a1f33;
    --ring-gold: #e9dcb8;
    --disc: #1f2a30;
    --gold-light: #f3d9a4;
    --gold-deep: #a8733a;
    --text-light: #f2eef7;
    --badge-hi: #c0106a;
    --badge-lo: #1c0512;
  }
  * { margin: 0; padding: 0; box-sizing: border-box; }
  html, body { width: 1200px; height: 1200px; overflow: hidden; background: var(--page); }

  .splash {
    position: absolute;
    left: 204px; top: 370px;
    width: 803px; height: 458px;
    border-radius: 30px;
    overflow: hidden;
    background: linear-gradient(100deg, var(--card-left) 0%, #5a4584 50%, var(--card-right) 100%);
  }
  .splash__backdrop {
    position: absolute; inset: 0;
    background:
      radial-gradient(circle at 50% 49%, rgba(190, 90, 255, .55) 0, rgba(160, 70, 230, .25) 190px, transparent 300px),
      radial-gradient(circle at 30% 40%, rgba(255,255,255,.06) 0, transparent 200px),
      radial-gradient(circle at 80% 70%, rgba(255,255,255,.05) 0, transparent 220px);
  }
  .splash__emblem { position: absolute; left: 0; top: 0; }
  .splash__number {
    font-family: "Playfair Display", serif;
    font-size: 142px;
    font-variant-numeric: lining-nums;
    font-feature-settings: "lnum" 1;
  }

  .brand-badge {
    position: absolute;
    left: 652px; top: 26px;
    width: 120px; height: 120px;
    border-radius: 50%;
    background: radial-gradient(circle at 45% 35%, var(--badge-hi) 0%, #6c0b3e 55%, var(--badge-lo) 100%);
    display: flex; align-items: center; justify-content: center;
  }
  .brand-badge__name {
    font-family: "Montserrat", sans-serif;
    font-weight: 700;
    font-size: 15px;
    letter-spacing: .5px;
    color: var(--text-light);
  }

  .release-mark {
    position: absolute;
    left: 0; width: 803px;
    text-align: center;
    color: var(--text-light);
    line-height: 1;
  }
  .release-mark__product {
    top: 259px;
    font-family: "Raleway", sans-serif;
    font-weight: 400;
    font-size: 35px;
  }
  .release-mark__edition {
    top: 301px;
    font-family: "Montserrat", sans-serif;
    font-size: 13px;
    letter-spacing: 3px;
  }

  .splash__date,
  .splash__tagline {
    position: absolute;
    top: 427px;
    font-family: "Montserrat", sans-serif;
    font-size: 13px;
    color: var(--text-light);
  }
  .splash__date { left: 39px; letter-spacing: 3px; }
  .splash__tagline { left: 354px; letter-spacing: .2px; }
</style>
</head>
<body>
  <main class="splash">
    <div class="splash__backdrop" role="img" aria-label="Soft purple technology backdrop of faint circuit traces and gears"></div>

    <svg class="splash__emblem" width="803" height="458" viewBox="0 0 803 458">
      <defs>
        <radialGradient id="disc-fill" cx="50%" cy="45%" r="55%">
          <stop offset="0" stop-color="#2b3a40"/>
          <stop offset="1" stop-color="#1f2a30"/>
        </radialGradient>
        <linearGradient id="steel-ring" x1="0" y1="0" x2="0" y2="1">
          <stop offset="0" stop-color="#7a8180"/>
          <stop offset=".5" stop-color="#3f4646"/>
          <stop offset="1" stop-color="#6c7372"/>
        </linearGradient>
        <linearGradient id="flare" x1="0" y1="0" x2="1" y2="0">
          <stop offset="0" stop-color="#ff7bd6" stop-opacity="0"/>
          <stop offset=".3" stop-color="#ffb0ea" stop-opacity=".8"/>
          <stop offset=".5" stop-color="#ffffff" stop-opacity="1"/>
          <stop offset=".7" stop-color="#ffb0ea" stop-opacity=".8"/>
          <stop offset="1" stop-color="#ff7bd6" stop-opacity="0"/>
        </linearGradient>
        <linearGradient id="gold" x1="0" y1="0" x2="0" y2="1">
          <stop offset=".1" stop-color="#f3d9a4"/>
          <stop offset=".6" stop-color="#c9995a"/>
          <stop offset="1" stop-color="#a8733a"/>
        </linearGradient>
        <radialGradient id="spark">
          <stop offset="0" stop-color="#ffffff"/>
          <stop offset=".4" stop-color="#ffffff" stop-opacity=".6"/>
          <stop offset="1" stop-color="#ffffff" stop-opacity="0"/>
        </radialGradient>
      </defs>
      <g aria-hidden="true">
        <circle cx="401" cy="228" r="180" fill="#b34dff" opacity=".35"/>
        <circle cx="401" cy="228" r="172" fill="#2a1f33"/>
        <circle cx="401" cy="228" r="158" fill="none" stroke="#e9dcb8" stroke-width="4"/>
        <circle cx="401" cy="228" r="138" fill="none" stroke="url(#steel-ring)" stroke-width="36"/>
        <circle cx="401" cy="228" r="118" fill="url(#disc-fill)" stroke="#11181b" stroke-width="3"/>
        <rect x="80" y="224" width="210" height="8" rx="4" fill="url(#flare)" opacity=".9"/>
        <rect x="513" y="224" width="210" height="8" rx="4" fill="url(#flare)" opacity=".9"/>
        <circle cx="240" cy="228" r="26" fill="url(#spark)"/>
        <circle cx="564" cy="228" r="26" fill="url(#spark)"/>
        <circle cx="414" cy="66" r="14" fill="url(#spark)"/>
      </g>
      <text class="splash__number" x="401" y="224" text-anchor="middle" fill="url(#gold)">4</text>
    </svg>

    <div class="brand-badge">
      <span class="brand-badge__name">TARNWELL</span>
    </div>

    <div class="release-mark release-mark__product">VELQUIRA</div>
    <div class="release-mark release-mark__edition">PREMIER EDITION</div>

    <p class="splash__date">JANUARY 21 2025</p>
    <p class="splash__tagline">Lorem ipsumrem</p>
  </main>
</body>
</html>
```